Kinetra Limbworks tri-fold brochure

Create a three panel brochure, front and back, for company named Kinetra Limbworks. It should have a modern and high-tech feel. It should appeal to not only patients but also physicians, physical therapists, and other medical personnel. Stock photos are fine but our logo must be included. You can also use the pictures from our website which is velmorastride.example or kinetralimb.example. They are the same website but we are rebranding for velmora stride to kinetra limbworks. Should also state "Hablamos Espanol" on the front of the brochure somewhere.
Updates

I have added pics and updated my profile. Sorry for the delay Added Monday, November 28, 2016

Target Market(s)

Amputees, Physicians, and Therapists

Industry/Entity Type

It Company

Requirements
Must have
• Kinetra Limbworks logo
• Office Locations:
• 4872 Wrenfield Drive, Ste 304
• Memphis, TN 38119
• Phone (555) 214-8830
• Fax (555) 214-8867
• 27904 Caskbridge Court, Ste B
• Houston, TX 77082
• Phone: (555) 630-4195
• Fax: (555)630-4172
• 8467 Quillory Street, Ste 200
• Arlington, TX 76015
• Phone: (555) 781-3046
• Fax: (555) 781-3019
• Hablamos EspaƱol
Nice to have
• Emphasis on patient care

```html
<!DOCTYPE html>
<html lang="en">
<head>
<meta charset="utf-8">
<title>Kinetra Limbworks – Tri-fold Brochure</title>
<link rel="stylesheet" href="https://fonts.googleapis.com/css2?family=Open+Sans:wght@400;600;700&family=Merriweather:wght@700;900&family=Roboto+Condensed:wght@700&family=Nunito:wght@800;900&display=swap">
<style>
  :root{
    --red:#e4112a;
    --red-dark:#b50c1f;
    --ink:#1f1f1f;
    --charcoal:#2a2829;
    --paper:#ffffff;
    --stage:#e6e7e9;
  }
  *{box-sizing:border-box;margin:0;padding:0}
  html,body{width:1200px;height:848px;overflow:hidden;background:var(--stage)}
  .brochure{position:absolute;left:40px;top:24px;width:1120px;height:800px;display:flex;box-shadow:0 10px 30px rgba(0,0,0,.18)}
  .panel{position:relative;width:373.33px;height:800px;background:var(--paper);overflow:hidden;font-family:"Open Sans",sans-serif;color:var(--ink)}
  .panel + .panel{border-left:1px solid #e2e2e2}
  .panel-art{position:absolute;inset:0;width:100%;height:100%}
  .tag{position:absolute;display:inline-block;background:var(--red);color:#fff;font-family:"Merriweather",serif;font-weight:900;font-size:17px;letter-spacing:.5px;padding:3px 12px;box-shadow:4px 0 0 var(--ink)}

  /* Panel 1 – mission */
  .mission-tag{left:34px;top:48px}
  .mission-copy{position:absolute;left:34px;top:92px;width:310px;font-size:12.2px;line-height:1.5;text-align:justify}
  .mission-copy p + p{margin-top:13px}
  .call-now{position:absolute;left:178px;top:388px;font-family:"Roboto Condensed",sans-serif;font-weight:700;color:var(--red);font-size:28px;line-height:1.05;white-space:nowrap}
  .perks{position:absolute;left:40px;top:640px;width:320px;list-style:none;color:#fff;font-size:15.5px;font-weight:600;line-height:1.45}
  .perks li::before{content:"* "}

  /* Panel 2 – locations */
  .office-tag{left:40px;top:48px}
  .office{position:absolute;font-size:12px;line-height:1.45}
  .office .addr{font-weight:600}
  .office .line{display:flex;align-items:center;gap:6px;font-size:14px}
  .office svg{flex:none}
  .office-memphis{left:30px;top:96px;width:160px}
  .office-houston{left:200px;top:96px;width:165px}
  .office-arlington{left:120px;top:236px;width:230px}

  /* name lockup */
  .wordmark{position:absolute;display:flex;align-items:center;gap:10px;font-family:"Open Sans",sans-serif;font-weight:700}
  .wordmark .dot{width:16px;height:16px;border-radius:50%;flex:none;background:var(--red)}
  .wordmark-back{left:0;right:0;top:600px;justify-content:center;color:#fff;font-size:24px}
  .wordmark-front{left:0;right:0;top:432px;justify-content:center;color:var(--red);font-size:26px}
  .web{position:absolute;left:0;right:0;text-align:center;letter-spacing:2.5px;font-size:15px;font-weight:600}
  .web-back{top:690px;color:#fff}
  .web-front{top:745px;color:#fff}

  /* Panel 3 – cover */
  .tagline{position:absolute;left:0;right:0;top:490px;text-align:center;font-family:"Nunito",sans-serif;font-weight:900;line-height:1.15}
  .tagline .lead{font-size:25px;color:var(--ink)}
  .tagline .sub{font-size:19px;color:var(--ink);font-weight:800}
  .tagline .punch{font-size:28px;color:var(--red)}
  .spanish{position:absolute;left:0;right:0;top:596px;text-align:center;font-family:"Open Sans",sans-serif;font-weight:700;font-size:15px;color:var(--ink);letter-spacing:.5px}
</style>
</head>
<body>
<main class="brochure">

  <!-- Inside left: mission -->
  <section class="panel panel-mission">
    <svg class="panel-art" viewBox="0 0 373 800" preserveAspectRatio="none" aria-hidden="true">
      <path d="M0 560 Q190 470 373 430 L373 462 Q190 505 0 600Z" fill="var(--charcoal)"/>
      <path d="M0 610 Q190 515 373 472 L373 800 L0 800Z" fill="var(--red)"/>
      <path d="M0 604 Q190 510 373 466" fill="none" stroke="#fff" stroke-width="5"/>
    </svg>
    <span class="tag mission-tag">MISSION</span>
    <div class="mission-copy">
      <p>To utilize education, experience and dedication in an effort to provide the most comprehensive prosthetic and orthotic care available.</p>
      <p>Our professionals are fully trained to evaluate, fabricate and fit every type of artificial limb and brace for the adult and pediatric population. We offer support and understanding as we counsel our patients in a safe and effective utilization of our devices. No two patients are the same at Kinetra Limbworks.</p>
      <p>We pride ourselves in treating every patient as an individual with dignity and respect. We guarantee high quality and fast turnaround on all our products.</p>
    </div>
    <div class="call-now">Call Us Now<br>555-214-8830</div>
    <svg style="position:absolute;left:22px;top:455px" width="190" height="190" viewBox="0 0 190 190" role="img" aria-label="Photo of a custom prosthetic socket with a decorative skull wrap">
      <circle cx="95" cy="95" r="93" fill="var(--red)"/>
      <circle cx="95" cy="95" r="86" fill="#fff"/>
      <defs><radialGradient id="socket" cx="50%" cy="45%" r="60%"><stop offset="0" stop-color="#8a3a1c"/><stop offset=".6" stop-color="#6b2a12"/><stop offset="1" stop-color="#3d1a0c"/></radialGradient></defs>
      <circle cx="95" cy="95" r="80" fill="url(#socket)"/>
    </svg>
    <ul class="perks">
      <li>Free consultations.</li>
      <li>Same Day Prosthetic Fitting Available</li>
      <li>Most items covered by Insurance</li>
      <li>We accept Medicare, Medicaid, and most private insurances.</li>
    </ul>
  </section>

  <!-- Back: office locations -->
  <section class="panel panel-locations">
    <svg class="panel-art" viewBox="0 0 373 800" preserveAspectRatio="none" aria-hidden="true">
      <path d="M0 480 Q190 440 373 400 L373 800 L0 800Z" fill="var(--charcoal)"/>
      <path d="M0 470 Q190 430 373 390 L373 400 Q190 440 0 480Z" fill="var(--red)"/>
    </svg>
    <span class="tag office-tag">Office Location:</span>
    <div class="office office-memphis">
      <div class="addr">4872 Wrenfield Drive,<br>Ste 304 Memphis,<br>TN 38119</div>
      <div class="line"><svg width="12" height="12" viewBox="0 0 12 12"><circle cx="6" cy="6" r="6" fill="var(--red)"/><path d="M3.5 3h1.6l.6 1.6-.9.6a4 4 0 0 0 1.9 1.9l.6-.9 1.6.6v1.6c-3 .3-5.7-2.4-5.4-5.4z" fill="#fff"/></svg>(555) 214-8830</div>
      <div class="line"><svg width="12" height="12" viewBox="0 0 12 12"><circle cx="6" cy="6" r="6" fill="var(--red)"/><rect x="3" y="4" width="6" height="4.5" rx=".6" fill="#fff"/></svg>(555) 214-8867</div>
    </div>
    <div class="office office-houston">
      <div class="addr">27904 Caskbridge Court,<br>Ste B<br>Houston, TX 77082</div>
      <div class="line"><svg width="12" height="12" viewBox="0 0 12 12"><circle cx="6" cy="6" r="6" fill="var(--red)"/><path d="M3.5 3h1.6l.6 1.6-.9.6a4 4 0 0 0 1.9 1.9l.6-.9 1.6.6v1.6c-3 .3-5.7-2.4-5.4-5.4z" fill="#fff"/></svg>(555) 630-4195</div>
      <div class="line"><svg width="12" height="12" viewBox="0 0 12 12"><circle cx="6" cy="6" r="6" fill="var(--red)"/><rect x="3" y="4" width="6" height="4.5" rx=".6" fill="#fff"/></svg>(555)630-4172</div>
    </div>
    <div class="office office-arlington">
      <div class="addr">8467 Quillory Street, Ste 200<br>Arlington, TX 76015</div>
      <div class="line"><svg width="12" height="12" viewBox="0 0 12 12"><circle cx="6" cy="6" r="6" fill="var(--red)"/><path d="M3.5 3h1.6l.6 1.6-.9.6a4 4 0 0 0 1.9 1.9l.6-.9 1.6.6v1.6c-3 .3-5.7-2.4-5.4-5.4z" fill="#fff"/></svg>(555) 781-3046</div>
      <div class="line"><svg width="12" height="12" viewBox="0 0 12 12"><circle cx="6" cy="6" r="6" fill="var(--red)"/><rect x="3" y="4" width="6" height="4.5" rx=".6" fill="#fff"/></svg>(555) 781-3019</div>
    </div>
    <svg style="position:absolute;left:88px;top:330px" width="200" height="200" viewBox="0 0 200 200" role="img" aria-label="Photo of a man with a running blade prosthesis seated on a block">
      <circle cx="100" cy="100" r="98" fill="var(--red)"/>
      <circle cx="100" cy="100" r="91" fill="#fff"/>
      <defs><radialGradient id="studio" cx="50%" cy="40%" r="65%"><stop offset="0" stop-color="#f4f4f4"/><stop offset=".7" stop-color="#c9c9c9"/><stop offset="1" stop-color="#8c8c8c"/></radialGradient></defs>
      <circle cx="100" cy="100" r="85" fill="url(#studio)"/>
    </svg>
    <div class="wordmark wordmark-back"><span class="dot"></span>Kinetra Limbworks</div>
    <div class="web web-back">www.kinetralimb.example</div>
  </section>

  <!-- Front cover -->
  <section class="panel panel-cover">
    <svg class="panel-art" viewBox="0 0 373 800" preserveAspectRatio="none" aria-hidden="true">
      <path d="M0 720 Q190 690 373 620 L373 800 L0 800Z" fill="var(--charcoal)"/>
    </svg>
    <svg style="position:absolute;left:-20px;top:0" width="420" height="420" viewBox="0 0 420 420" role="img" aria-label="Photo of a woman with a prosthetic leg running on the beach with her dog">
      <path d="M60 300 A175 175 0 1 0 90 60" fill="none" stroke="var(--charcoal)" stroke-width="14"/>
      <circle cx="215" cy="205" r="185" fill="var(--red)"/>
      <circle cx="210" cy="200" r="172" fill="#fff"/>
      <defs><linearGradient id="beach" x1="0" y1="0" x2="0" y2="1"><stop offset="0" stop-color="#7fb6e8"/><stop offset=".42" stop-color="#bcd9ef"/><stop offset=".5" stop-color="#e9e4d8"/><stop offset="1" stop-color="#f5efe2"/></linearGradient></defs>
      <circle cx="210" cy="200" r="164" fill="url(#beach)"/>
    </svg>
    <div class="wordmark wordmark-front"><span class="dot"></span>Kinetra Limbworks</div>
    <div class="tagline">
      <div class="lead">Stepping forward</div>
      <div class="sub">to help you do the things</div>
      <div class="punch">That you want to do!</div>
    </div>
    <div class="spanish">Hablamos Español</div>
    <div class="web web-front">www.kinetralimb.example</div>
  </section>

</main>
</body>
</html>
```